Brisk Lending Benefits Summary

We are looking to put our benefits information into a summary document and make it look pretty/easy to read! I put all of the information together into a document, one tab for all of our medical plans and another for dental/vision. This document is only there as a guide. I want this to be visually appealing, so feel free to get creative with the format.

Industry/Entity Type

Mortgage Lender

Colors
31b7a3
ffcf3e

Requirements
Should not have
• I don't want a copy and pasted version of the visual I sent, with our logo attached.

```html
<!DOCTYPE html>
<html lang="en">
<head>
<meta charset="utf-8">
<title>Brisk Lending Benefits Summary</title>
<link href="https://fonts.googleapis.com/css2?family=Montserrat:wght@600;700;800&family=Open+Sans:wght@400;600;700&family=Roboto+Condensed:wght@700&display=swap" rel="stylesheet">
<style>
:root{
  --teal:#33b5c6;
  --yellow:#f4d22b;
  --ink:#2b2b2b;
  --grey:#e4e4e5;
  --grey-light:#efeff0;
  --line:#7a7a7a;
  --paper:#ffffff;
  --bg:#ffffff;
}
*{box-sizing:border-box;margin:0;padding:0}
html,body{width:1200px;height:900px;overflow:hidden;background:var(--bg)}
body{position:relative;font-family:"Open Sans",sans-serif;color:var(--ink)}
.page{position:absolute;top:112px;width:474px;height:672px;background:var(--paper);box-shadow:0 0 3px rgba(0,0,0,.35)}
.page--medical{left:101px}
.page--extras{left:621px}

/* header */
.brand{position:absolute;left:20px;top:30px;width:140px;display:flex;align-items:center;gap:6px}
.brand__mark{width:12px;height:12px;background:var(--yellow);flex:none}
.brand__name{font-family:"Montserrat",sans-serif;font-weight:700;font-size:21px;line-height:1;color:var(--teal)}
.hero{position:absolute;left:168px;top:0;right:0;height:95px;background:var(--teal);padding:15px 0 0 26px}
.hero__title{font-family:"Montserrat",sans-serif;font-weight:800;font-size:39px;line-height:1;color:#fff;letter-spacing:2px}
.hero__sub{font-family:"Montserrat",sans-serif;font-weight:800;font-size:22px;line-height:1;color:var(--yellow);margin-top:6px;letter-spacing:1.2px}

/* medical table */
.plans{position:absolute;left:21px;top:107px;width:431px;border:1.5px solid var(--line);border-radius:8px;overflow:hidden}
.plans table{width:100%;border-collapse:collapse;table-layout:fixed;font-size:5.2px;line-height:1.2}
.plans td,.plans th{border:0.6px solid var(--line);text-align:center;vertical-align:middle;color:#444;padding:0 1px}
.plans tr:first-child th{border-top:none}
.plans th:first-child,.plans td:first-child{border-left:none}
.plans th:last-child,.plans td:last-child{border-right:none}
.plans tr:last-child td{border-bottom:none}
.plans .plan-name{background:var(--teal);color:#fff;font-family:"Roboto Condensed",sans-serif;font-weight:700;font-size:4.2px;height:17px}
.plans .net{background:var(--yellow);color:var(--teal);font-weight:600;font-size:4.4px;height:15px}
.plans .label{text-align:left;padding:0 4px;font-size:5.6px;color:var(--teal)}
.plans .label b{color:var(--ink);font-weight:600}
.plans .cost{vertical-align:top;padding-top:16px;font-size:5.6px;line-height:1.85}
.footnote{position:absolute;left:21px;top:610px;width:432px;font-size:6.6px;line-height:1.32;color:var(--ink)}

/* vision */
.vision{position:absolute;left:21px;top:32px;width:429px;height:387px;background:var(--grey-light);border-radius:10px;overflow:hidden}
.vision table{width:100%;border-collapse:collapse;table-layout:fixed;font-size:5.8px;line-height:1.5}
.vision td{text-align:left;vertical-align:middle;padding:0 7px}
.vision .band{background:var(--yellow);height:28px;color:var(--teal);font-family:"Montserrat",sans-serif;font-weight:700;font-size:8.5px;vertical-align:bottom;padding-bottom:4px}
.vision .alt{background:var(--grey)}
.vision .div{border-left:1px solid var(--ink)}
.vision b{font-weight:700;font-size:6.8px}
.tab{position:absolute;height:24px;background:var(--teal);color:#fff;font-family:"Montserrat",sans-serif;font-weight:700;font-size:17px;text-align:center;line-height:24px}
.tab--vision{left:54px;top:22px;width:98px}
.tab--dental{left:54px;top:426px;width:98px;background:var(--yellow)}
.tab::before{content:"";position:absolute;left:-5px;top:0;border-bottom:5px solid #1e8f9e;border-left:5px solid transparent}

/* dental */
.dental{position:absolute;left:21px;top:435px;width:431px;height:219px;background:var(--grey-light);border-radius:10px;overflow:hidden}
.dental table{width:100%;border-collapse:collapse;table-layout:fixed;font-size:5.8px;line-height:1.35}
.dental td{padding:0 6px;text-align:left;vertical-align:middle}
.dental .head td{background:var(--teal);color:#fff;font-weight:700;font-size:7.2px;height:19px;text-align:center}
.dental .sub td{color:var(--teal);font-size:5.8px;height:14px;text-align:center;border-bottom:0.6px solid var(--line)}
.dental .lbl{color:var(--teal)}
.dental .alt td{background:var(--grey)}
.dental .vl{border-left:0.6px solid var(--line)}
.dental .title td{text-align:center;height:14px;border-bottom:0.6px solid var(--line);font-size:5.8px}
</style>
</head>
<body>

<section class="page page--medical">
  <div class="brand"><span class="brand__mark"></span><span class="brand__name">brisk lending</span></div>
  <div class="hero">
    <div class="hero__title">MORTGAGE</div>
    <div class="hero__sub">WITHOUT THE MESS</div>
  </div>

  <div class="plans">
    <table>
      <colgroup><col style="width:60px"><col span="10"></colgroup>
      <tr>
        <th class="plan-name"></th>
        <th class="plan-name" colspan="2">Tallowbrook Gold PPO<br>2250/0%/2250 w/HSA TradRX</th>
        <th class="plan-name" colspan="2">Tallowbrook Silver PPO<br>3500/50%/7900 TradRX</th>
        <th class="plan-name" colspan="2">Tallowbrook Gold Pathway<br>HMO 1000/20%/5600</th>
        <th class="plan-name" colspan="2">Tallowbrook Gold PPO<br>750/20%/5250</th>
        <th class="plan-name" colspan="2">Tallowbrook Platinum PPO<br>250/20%/3500</th>
      </tr>
      <tr>
        <th class="net"></th>
        <th class="net">In-Network</th><th class="net">Non-Network</th>
        <th class="net">In-Network</th><th class="net">Non-Network</th>
        <th class="net">In-Network</th><th class="net">Non-Network</th>
        <th class="net">In-Network</th><th class="net">Non-Network</th>
        <th class="net">In-Network</th><th class="net">Non-Network</th>
      </tr>
      <tr style="height:22px">
        <td class="label">Annual Deductible<br><b style="font-weight:400">Single / Family</b></td>
        <td>$2,250/<br>$4,500</td><td>$6,750/<br>$13,500</td><td>$3,500/<br>$7,000</td><td>$10,500/<br>$21,000</td><td>$1,000/<br>$3,000</td><td>Not<br>covered</td><td>$750/<br>$2,250</td><td>$2,250/<br>$4,500</td><td>$250 / $750</td><td>$2,000/<br>$4,000</td>
      </tr>
      <tr style="height:27px">
        <td class="label">Annual Out-of-<br>Pocket Maximum<br><b style="font-weight:400">Single / Family</b></td>
        <td>$2,250/<br>$4,500</td><td>$7,875/<br>$15,750</td><td>$7,900 /<br>$15,800</td><td>$23,700/<br>$47,400</td><td>$5,600/<br>$11,200</td><td>Not<br>covered</td><td>$5,250/<br>$10,500</td><td>$15,750/<br>$31,500</td><td>$3,500/<br>$7,000</td><td>$10,500/<br>$21,000</td>
      </tr>
      <tr style="height:42px">
        <td class="label"><b>Office Visit</b><br>Primary Care<br><br>Specialist</td>
        <td>0%<br>coinsurance<br>0%<br>coinsurance</td><td>50%<br>coinsurance<br>50%<br>coinsurance</td><td>$50/visit<br><br>$75/visit</td><td>50%<br>coinsurance<br>50%<br>coinsurance</td><td>$25/visit<br><br>$50/visit</td><td>Not<br>covered</td><td>$20/visit for<br>first 3, then<br>20%<br>coinsurance</td><td>50%<br>coinsurance<br>50%<br>coinsurance</td><td>$15/visit<br><br>$75/visit</td><td>50%<br>coinsurance<br>50%<br>coinsurance</td>
      </tr>
      <tr style="height:23px">
        <td class="label">Preventative<br>Services</td>
        <td>No charge</td><td>50%<br>coinsurance</td><td>No<br>charge</td><td>50%<br>coinsurance</td><td>No<br>charge</td><td>Not<br>covered</td><td>No<br>charge</td><td>50%<br>coinsurance</td><td>No<br>charge</td><td>50%<br>coinsurance</td>
      </tr>
      <tr style="height:24px">
        <td class="label">Diagnostic Test &amp;<br>Imaging</td>
        <td>0%<br>coinsurance</td><td>50%<br>coinsurance</td><td>50%<br>coinsurance</td><td>50%<br>coinsurance</td><td>20%<br>coinsurance</td><td>Not<br>covered</td><td>20%<br>coinsurance</td><td>50%<br>coinsurance</td><td>20%<br>coinsurance</td><td>50%<br>coinsurance</td>
      </tr>
      <tr style="height:22px">
        <td class="label">Outpatient Surgery</td>
        <td>0%<br>coinsurance</td><td>50%<br>coinsurance</td><td>50%<br>coinsurance</td><td>50%<br>coinsurance</td><td>20%<br>coinsurance</td><td>Not<br>covered</td><td>20%<br>coinsurance</td><td>50%<br>coinsurance</td><td>20%<br>coinsurance</td><td>50%<br>coinsurance</td>
      </tr>
      <tr style="height:50px">
        <td class="label"><b>Emergency</b><br>Emergency Room<br>Emergency<br>Transportation<br>Urgent Care</td>
        <td>0%<br>coinsurance<br>0%<br>coinsurance<br>0%<br>coinsurance</td><td>Covered as<br>In-Network<br>Covered as<br>In-Network<br>50%<br>coinsurance</td><td>Covered as<br>In-Network<br>Covered as<br>In-Network<br>50%<br>coinsurance</td><td>Covered as<br>In-Network<br>Covered as<br>In-Network<br>50%<br>coinsurance</td><td>$300 visit<br><br>20%<br>coinsurance<br><br>$50/visit</td><td>Not<br>covered<br>Not<br>covered<br>Not<br>covered</td><td>$300/visit<br><br>$300/trip<br><br>20%<br>coinsurance</td><td>Covered as<br>In-Network<br>Covered as<br>In-Network<br>50%<br>coinsurance</td><td>$300 visit<br><br>20%<br>coinsurance<br><br>$50/visit</td><td>Covered as<br>In-Network<br>Covered as<br>In-Network<br>50%<br>coinsurance</td>
      </tr>
      <tr style="height:22px">
        <td class="label">Hospital stay</td>
        <td>0%<br>coinsurance</td><td>50%<br>coinsurance</td><td>50%<br>coinsurance</td><td>50%<br>coinsurance</td><td>20%<br>coinsurance</td><td>Not<br>covered</td><td>20%<br>coinsurance</td><td>50%<br>coinsurance</td><td>20%<br>coinsurance</td><td>50%<br>coinsurance</td>
      </tr>
      <tr style="height:62px">
        <td class="label"><b>Mental Health/<br>Behavioral Health/<br>Substance Abuse<br>Services</b><br><br>Outpatient Services<br><br>Inpatient Services</td>
        <td>Office Visit<br>0%<br>coinsurance<br>Other<br>Outpatient<br>0%<br>coinsurance</td><td>Office Visit<br>50%<br>coinsurance<br>Other<br>Outpatient<br>50%<br>coinsurance</td><td>Office Visit<br>$50/visit<br>Other<br>Outpatient<br>50%<br>coinsurance</td><td>Office Visit<br>50%<br>coinsurance<br>Other<br>Outpatient<br>50%<br>coinsurance</td><td>Office Visit<br>50%<br>coinsurance<br>Other<br>Outpatient<br>50%<br>coinsurance</td><td>Not<br>covered<br><br><br><br>Not<br>covered</td><td>Office Visit<br>$20/visit<br>for first 3,<br>then 20%<br>coinsurance<br>Other<br>Outpatient</td><td>Office Visit<br>50%<br>coinsurance<br>Other<br>Outpatient<br>50%<br>coinsurance</td><td>Office Visit<br>$15/visit<br>Other<br>Outpatient<br>20%<br>coinsurance</td><td>Office Visit<br>50%<br>coinsurance<br>Other<br>Outpatient<br>50%<br>coinsurance</td>
      </tr>
      <tr style="height:49px">
        <td class="label"><b>Pregnancy</b><br>Office visits,<br>childbirth delivery<br><br>professional &amp;<br>facilityservices</td>
        <td>0%<br>coinsurance</td><td>50%<br>coinsurance</td><td>50%<br>coinsurance</td><td>50%<br>coinsurance</td><td>20%<br>coinsurance</td><td>Not<br>covered</td><td>20%<br>coinsurance</td><td>50%<br>coinsurance</td><td>20%<br>coinsurance</td><td>50%<br>coinsurance</td>
      </tr>
      <tr style="height:108px">
        <td class="label" style="vertical-align:top;padding-top:4px"><b style="font-weight:400">Monthly Cost<br>(Varies by Age)*</b><br>Age 30<br>Employee<br>Per Child Cost**<br>Spouse/Domestic<br>Partner Cost<br><br>Age 50<br>Employee<br>Per Child Cost**<br>Spouse/Domestic<br>Partner Cost</td>
        <td colspan="2" class="cost">$134<br>$181<br>$268<br><br><br>$211<br>$181<br>$422</td>
        <td colspan="2" class="cost">$111<br>$150<br>$222<br><br><br>$175<br>$150<br>$350</td>
        <td colspan="2" class="cost">$114<br>$155<br>$229<br><br><br>$180<br>$155<br>$361</td>
        <td colspan="2" class="cost">$136<br>$184<br>$273<br><br><br>$215<br>$184<br>$431</td>
        <td colspan="2" class="cost">$149<br>$201<br>$299<br><br><br>$235<br>$201<br>$471</td>
      </tr>
    </table>
  </div>

  <p class="footnote">Limitations, exceptions and other important information are provided in the summary of benefits and coverage for each plan. In the event that the information in this summary differs from the plan description, the plan description will prevail. *For the purpose of this document, we assume that your spouse is the same age as you and that your children are 18 years old or less. Your quoted price will change based on the actual age of your spouse and children. **Children beyond the first three are covered at no additional cost.</p>
</section>

<section class="page page--extras">
  <div class="vision">
    <table>
      <colgroup><col style="width:157px"><col style="width:167px"><col></colgroup>
      <tr><td class="band"></td><td class="band div">In-Network</td><td class="band div" style="text-align:center">Non-Network</td></tr>
      <tr class="alt" style="height:52px"><td><b>Co-Pay</b><br>First Service Provided<br>Exams<br>Materials</td><td class="div" colspan="2">Not applicable<br>exams $10.00<br>$25<br>Waived for conventional &amp; planned replacement contact lensesMaterials</td></tr>
      <tr style="height:56px"><td><b>How Often Can I Obtain Service?*</b><br>Exams<br>Lenses<br>Frames<br>Materials</td><td class="div"><br>Once/year<br>Once/year<br>Once every other year<br>Once/year</td><td class="div"></td></tr>
      <tr class="alt" style="height:17px"><td>Eye exam</td><td class="div">Copay applies</td><td class="div" style="padding-left:20px">Amount over $39</td></tr>
      <tr style="height:46px"><td>Single Vision<br>Lined bifocal<br>Lined Trifocal<br>Lenticular</td><td class="div">Copay applies<br>Copay applies<br>Copay applies<br>Copay applies</td><td class="div" style="padding-left:20px">Amount over $23<br>Amount over $37<br>Amount over $49<br>Amount over $64</td></tr>
      <tr class="alt" style="height:53px"><td><b>Contact Lense</b><br>Conventional<br>Planned Replacement &amp; Disposable<br>Medically Necessary<br>Evaulation &amp; Fitting</td><td class="div">Amount over $130<br>Amount over $130<br>Copay applies<br>15% off professional fee</td><td class="div" style="padding-left:20px">Amount over $100<br>Amount over $100<br>Amount over $210<br>Not covered</td></tr>
      <tr style="height:21px"><td>Frames</td><td class="div">$130, 20% discount on amount over $130</td><td class="div" style="padding-left:20px">Amount over $46</td></tr>
      <tr class="alt" style="height:19px"><td>Lens &amp; Frame Allowance</td><td class="div">No discounts</td><td class="div" style="padding-left:20px">No discounts</td></tr>
      <tr style="height:23px"><td>Cosmetic Extras</td><td class="div">Discounted at average 20%-25% off providers UCR</td><td class="div" style="padding-left:20px">No discounts</td></tr>
      <tr class="alt" style="height:25px"><td>Laser Correction Surgery</td><td class="div">Average 15% discount off usual price or 5% off promotional price</td><td class="div" style="padding-left:20px">No discounts</td></tr>
      <tr style="height:47px"><td><b>Monthly Cost</b><br>Employee<br>Child Cost***<br>Spouse/Domestic Partner Cost</td><td class="div" colspan="2" style="padding-left:160px"><br>$9<br>$7<br>$6</td></tr>
    </table>
  </div>
  <div class="tab tab--vision">Vision</div>

  <div class="dental">
    <table>
      <colgroup><col style="width:165px"><col style="width:63px"><col style="width:69px"><col style="width:68px"><col></colgroup>
      <tr class="head"><td style="background:var(--teal)"></td><td colspan="2" class="vl">Calendar Year Deductible</td><td colspan="2" class="vl">Coinsurance (Policy Pays)</td></tr>
      <tr class="sub"><td style="border-bottom:none"></td><td class="vl">In-Network</td><td class="vl">Non-Network</td><td class="vl">In-Network</td><td class="vl">Non-Network</td></tr>
      <tr class="alt" style="height:15px"><td class="lbl">Preventative</td><td class="vl">$0</td><td class="vl">$0</td><td class="vl">100%</td><td class="vl">100%</td></tr>
      <tr style="height:15px"><td class="lbl">Basic</td><td class="vl">$50</td><td class="vl">$50</td><td class="vl">80%</td><td class="vl">80%</td></tr>
      <tr class="alt" style="height:15px"><td class="lbl">Major</td><td class="vl">$50</td><td class="vl">$50</td><td class="vl">50%</td><td class="vl">50%</td></tr>
      <tr style="height:26px"><td class="lbl">Combined Family Deductible</td><td class="vl" colspan="4">Max deductible 3 times the per person deductible amount. Deductibles for basic and major procedures are combined for in-network and non-network.</td></tr>
      <tr class="alt" style="height:22px"><td class="lbl">Combined Maximum</td><td class="vl" colspan="4">Maximums for preventative, basic, and major procedures combined. Innetwork and non-network maximums are $1,000 per person.</td></tr>
      <tr class="title"><td colspan="5">Orthodontia - Child</td></tr>
      <tr class="sub"><td style="border-bottom:none"></td><td class="vl">In-Network</td><td class="vl">Non-Network</td><td class="vl">In-Network</td><td class="vl">Non-Network</td></tr>
      <tr class="alt" style="height:22px"><td class="lbl">Lifetime Deductible<br>Lifetime Maximum</td><td class="vl">$0<br>$1,000</td><td class="vl">$0<br>$1,000</td><td class="vl">50%</td><td class="vl">50%</td></tr>
      <tr style="height:42px"><td><span class="lbl">Monthly cost</span><br>Employee<br>Child Cost<br>Spouse/Domestic Partner Cost</td><td class="vl" colspan="4" style="padding-left:128px"><br>$40<br>$68<br>$41</td></tr>
    </table>
  </div>
  <div class="tab tab--dental">Dental</div>
</section>

</body>
</html>
```